looking to have a web site for the company which provides services in the industrial and commercial sectors such as: electrical, automation control and system integration, construction and maintenance, millwright, equipment assembly repair and installation. I have the domain already brivanholdings.net and logo. Most recent projects fulfilled for the following clients: MarlowKibbleCo, Dunholt University, OKSU, FALSTO, Tazzik, Prairie Grains

Target Market(s)

industrial and commercial sectors in electrical, automation, millwright and fabrication fields

Industry/Entity Type

Industrial

Coding

Coded - Design and coding required

Number of Pages Required

5+ page

Font styles to use
Sans Serif

Colors

Designer to choose colors to be used in the design.

Requirements
Nice to have
• looking to get something not complicated, nicely presented with minimum or no scrolling

```html
<!DOCTYPE html>
<html lang="en">
<head>
<meta charset="utf-8">
<title>Brivan Holdings – Industrial Electrical Services</title>
<link href="https://fonts.googleapis.com/css2?family=Open+Sans:wght@400;600;700&family=Raleway:wght@400;600;700;800&display=swap" rel="stylesheet">
<style>
:root{
  --blue:#1ba0e1;
  --blue-dark:#0f7fc0;
  --navy:#0e2b45;
  --navy-deep:#0a2238;
  --ink:#2b2f33;
  --muted:#7b8287;
  --line:#e3e7ea;
  --pale:#f4f7f9;
  --white:#ffffff;
}
*{box-sizing:border-box;margin:0;padding:0}
html,body{width:1200px;height:2980px;overflow:hidden}
body{font-family:"Open Sans",Arial,sans-serif;color:var(--ink);background:var(--white);position:relative}
h1,h2,h3,.brand,.nav{font-family:"Raleway",Arial,sans-serif}

/* header */
.site-header{height:120px;position:relative;display:flex;align-items:center;padding:0 80px}
.brand{display:flex;flex-direction:column;line-height:1}
.brand-name{font-size:42px;font-weight:800;color:var(--blue);letter-spacing:1px}
.brand-sub{font-size:20px;font-weight:700;color:var(--blue);letter-spacing:4px;margin-top:4px}
.nav{margin-left:auto;display:flex;gap:0;margin-top:26px}
.nav a{font-size:15px;font-weight:600;color:var(--ink);text-decoration:none;padding:10px 22px;border-left:1px solid var(--line)}
.nav a:first-child{border-left:none}
.quote-btn{position:absolute;top:0;right:20px;background:var(--blue);color:var(--white);font-weight:700;font-size:15px;padding:12px 18px;text-decoration:none}

/* hero */
.hero{height:540px;position:relative;overflow:hidden;background:linear-gradient(120deg,#c8d3db 0%,#9fb2c1 45%,#6f8ba0 100%)}
.hero-photo{position:absolute;inset:0}
.hero-panel{position:absolute;right:0;top:0;width:640px;height:100%;background:rgba(27,160,225,.82);clip-path:polygon(24% 0,100% 0,100% 100%,0 100%)}
.hero-text{position:absolute;left:740px;top:210px;color:var(--white)}
.hero-text h1{font-size:54px;font-weight:800;letter-spacing:1px}
.hero-text p{font-family:"Raleway",sans-serif;font-size:34px;font-weight:400;margin-top:8px}
.hero-arrow{position:absolute;top:250px;width:30px;height:50px}
.hero-arrow.left{left:14px}.hero-arrow.right{right:14px}

/* welcome */
.welcome{height:420px;padding:80px 80px 0;display:flex;gap:60px}
.welcome-copy{width:680px}
.section-title{font-size:34px;font-weight:700;color:var(--ink)}
.rule{display:block;width:70px;height:3px;background:var(--blue);margin:14px 0 22px}
.welcome-copy p{font-size:14px;line-height:24px;color:var(--muted);margin-bottom:16px}
.btn{display:inline-block;background:var(--blue);color:var(--white);font-size:14px;font-weight:600;padding:10px 22px;text-decoration:none}
.welcome-media{position:relative;width:320px;height:290px;margin-top:10px}
.welcome-media .frame{position:absolute;left:0;top:0;width:300px;height:270px;background:var(--blue)}
.welcome-media .photo{position:absolute;left:20px;top:20px;width:300px;height:270px;background:linear-gradient(135deg,#d9dfe4,#8ea3b3)}

/* services */
.services{height:460px;display:flex;position:relative}
.services-photo{width:500px;height:440px;background:linear-gradient(135deg,#4d6d85,#233f57 60%,#3b5c74);clip-path:polygon(0 0,100% 0,68% 100%,0 100%)}
.services-body{padding:20px 0 0 40px}
.services-grid{display:grid;grid-template-columns:repeat(3,160px);gap:20px 24px;margin-top:6px}
.service{height:170px;border:1px solid var(--line);display:flex;flex-direction:column;align-items:center;padding-top:26px;text-align:center;box-shadow:0 2px 6px rgba(0,0,0,.05)}
.service svg{width:62px;height:62px}
.service h3{font-size:17px;font-weight:700;margin-top:16px;line-height:22px;color:var(--ink)}

/* what we do */
.what{height:440px;margin-top:40px;background:var(--blue);position:relative;display:flex;padding:50px 0 0 80px}
.what-copy{width:420px;color:var(--white)}
.what-copy .section-title{color:var(--white);font-size:38px}
.what-copy .rule{background:var(--white)}
.what-copy p{font-size:14px;line-height:24px;opacity:.95;margin-bottom:26px}
.btn-dark{background:var(--navy);}
.what-video{position:absolute;right:80px;top:20px;width:560px;height:400px;border:8px solid var(--white);background:linear-gradient(135deg,#8d9a8f,#56665e 55%,#a3a58f)}
.play{position:absolute;left:50%;top:50%;width:70px;height:70px;transform:translate(-50%,-50%)}

/* blog */
.blog{height:560px;padding:60px 80px 0}
.blog-grid{display:flex;gap:20px;margin-top:10px}
.post{width:510px;position:relative;box-shadow:0 2px 8px rgba(0,0,0,.08)}
.post-photo{height:210px;background:linear-gradient(135deg,#9aa5ad,#4f5f6b)}
.post:last-child .post-photo{background:linear-gradient(135deg,#d6dadc,#98a1a6)}
.date{position:absolute;left:0;top:30px;width:78px;text-align:center;font-family:"Raleway",sans-serif}
.date .day{background:var(--blue);color:var(--white);font-size:18px;font-weight:700;padding:6px 0}
.date .year{background:var(--white);color:var(--ink);font-size:16px;font-weight:700;padding:8px 0}
.date .count{background:var(--blue);color:var(--white);font-size:13px;padding:4px 0}
.post-body{background:var(--navy);color:var(--white);padding:20px 22px 14px}
.post-body h3{font-size:22px;font-weight:700}
.post-body p{font-size:13px;line-height:21px;opacity:.8;margin-top:8px}
.post-meta{display:flex;justify-content:space-between;background:var(--navy-deep);color:#c9d4dc;font-size:13px;padding:12px 22px}
.post-meta a{color:var(--blue);text-decoration:none}

/* clients */
.clients{height:220px;background:var(--pale);text-align:center;padding-top:30px}
.clients h2{font-size:32px;font-weight:700;color:var(--blue)}
.client-row{display:flex;justify-content:space-between;align-items:center;padding:40px 60px 0}
.client{display:flex;align-items:center;gap:10px;font-family:"Open Sans",sans-serif;font-weight:700;font-size:20px;color:var(--navy)}
.client i{display:block;width:16px;height:16px;background:var(--blue)}
.client-arrow{width:16px;height:28px}

/* footer */
.site-footer{height:200px;background:var(--navy);color:#c6d2db;display:flex;padding:36px 80px 0;gap:60px;font-size:13px}
.footer-brand .brand-name{font-size:34px;color:var(--white)}
.footer-brand .brand-sub{font-size:15px;color:var(--white)}
.footer-brand p{margin-top:12px;width:230px;line-height:20px}
.site-footer h3{font-size:18px;color:var(--white);font-weight:700;margin-bottom:14px}
.contact li{list-style:none;display:flex;align-items:center;gap:10px;margin-bottom:10px}
.contact svg{width:14px;height:14px}
.footer-right{margin-left:auto}
.footer-nav{display:flex;gap:30px;margin-bottom:26px}
.footer-nav a{color:#c6d2db;text-decoration:none;font-size:14px}
.newsletter{display:flex;margin-top:4px}
.newsletter span{display:block;width:300px;height:36px;background:var(--white);color:#999;padding:9px 12px}
.newsletter b{background:var(--blue);color:var(--white);padding:9px 18px;font-weight:600}
</style>
</head>
<body>

<header class="site-header">
  <div class="brand">
    <span class="brand-name">BRIVAN</span>
    <span class="brand-sub">HOLDINGS LTD</span>
  </div>
  <nav class="nav">
    <a href="#">HOME</a><a href="#">ABOUT US</a><a href="#">SERVICES</a><a href="#">OUR PROJECTS</a><a href="#">CONTACT US</a>
  </nav>
  <a class="quote-btn" href="#">Get a Quote?</a>
</header>

<section class="hero">
  <div class="hero-photo" role="img" aria-label="Electrician in hard hat and safety vest standing in an industrial plant"></div>
  <div class="hero-panel"></div>
  <div class="hero-text">
    <h1>BRIVAN HOLDINGS</h1>
    <p>Provide Best Electrical Services</p>
  </div>
  <svg class="hero-arrow left" viewBox="0 0 30 50"><path d="M24 4 6 25l18 21" fill="none" stroke="#fff" stroke-width="4"/></svg>
  <svg class="hero-arrow right" viewBox="0 0 30 50"><path d="M6 4l18 21L6 46" fill="none" stroke="#fff" stroke-width="4"/></svg>
</section>

<section class="welcome">
  <div class="welcome-copy">
    <h2 class="section-title">Welcome to Brivan Holdings</h2>
    <span class="rule"></span>
    <p>We deliver electrical, automation and mechanical work for industrial and commercial clients. Our crews plan, install and maintain systems that keep plants running safely, on schedule and within budget. From a single panel upgrade to a full production line, we bring trained people, sound methods and clear reporting to every job we take on.</p>
    <p>Founded by field technicians, the company has grown through repeat work and referrals. We hold ourselves to strict safety standards, document every step and stay on call after handover so each client knows who to reach when something needs attention.</p>
    <a class="btn" href="#">READ MORE</a>
  </div>
  <div class="welcome-media">
    <div class="frame"></div>
    <div class="photo" role="img" aria-label="Engineer in hard hat working at an electrical control panel"></div>
  </div>
</section>

<section class="services">
  <div class="services-photo" role="img" aria-label="Close view of industrial switchgear and wiring cabinets"></div>
  <div class="services-body">
    <h2 class="section-title">Our Services</h2>
    <span class="rule"></span>
    <div class="services-grid">
      <div class="service">
        <svg viewBox="0 0 62 62"><path d="M31 4 18 58M31 4l13 54M22 40h18M25 26h12M10 18h42M14 18l-4 8M48 18l4 8" fill="none" stroke="#1ba0e1" stroke-width="3"/></svg>
        <h3>Electrical</h3>
      </div>
      <div class="service">
        <svg viewBox="0 0 62 62"><rect x="8" y="14" width="46" height="36" fill="none" stroke="#1ba0e1" stroke-width="3"/><circle cx="31" cy="32" r="9" fill="none" stroke="#1ba0e1" stroke-width="3"/><path d="M31 18v5M31 41v5M17 32h5M40 32h5" stroke="#1ba0e1" stroke-width="3"/></svg>
        <h3>Automation<br>Control</h3>
      </div>
      <div class="service">
        <svg viewBox="0 0 62 62"><rect x="12" y="8" width="38" height="12" fill="#1ba0e1"/><rect x="12" y="25" width="38" height="12" fill="#1ba0e1"/><rect x="12" y="42" width="38" height="12" fill="#1ba0e1"/><circle cx="43" cy="14" r="2" fill="#fff"/><circle cx="43" cy="31" r="2" fill="#fff"/><circle cx="43" cy="48" r="2" fill="#fff"/></svg>
        <h3>System<br>Integration</h3>
      </div>
      <div class="service">
        <svg viewBox="0 0 62 62"><path d="M12 50 36 26M38 10a12 12 0 0 0 14 14l-8 4-6-6z" fill="none" stroke="#1ba0e1" stroke-width="5" stroke-linecap="round"/><path d="M14 14l34 34" stroke="#1ba0e1" stroke-width="5" stroke-linecap="round"/></svg>
        <h3>Construction<br>and Maintenance</h3>
      </div>
      <div class="service">
        <svg viewBox="0 0 62 62"><circle cx="31" cy="31" r="16" fill="none" stroke="#1ba0e1" stroke-width="8" stroke-dasharray="8 4.5"/><circle cx="31" cy="31" r="6" fill="#1ba0e1"/></svg>
        <h3>Millwright</h3>
      </div>
      <div class="service">
        <svg viewBox="0 0 62 62"><path d="M22 6v14a9 9 0 0 0 18 0V6M31 29v22" fill="none" stroke="#1ba0e1" stroke-width="5" stroke-linecap="round"/><circle cx="31" cy="54" r="4" fill="#1ba0e1"/></svg>
        <h3>Equipment assembly repair and installation</h3>
      </div>
    </div>
  </div>
</section>

<section class="what">
  <div class="what-copy">
    <h2 class="section-title">What We Do</h2>
    <span class="rule"></span>
    <p>We design, build and service electrical and control systems for plants, warehouses and public buildings. Our teams handle wiring, motor controls, PLC programming, conveyor alignment and equipment moves, working around production so downtime stays low. Every project closes with tested drawings, trained staff and a support plan that fits the site.</p>
    <a class="btn btn-dark" href="#">Learn More</a>
  </div>
  <div class="what-video" role="img" aria-label="Video still of a large industrial processing hall with steel piping">
    <svg class="play" viewBox="0 0 70 70"><path d="M24 16v38l32-19z" fill="#fff"/></svg>
  </div>
</section>

<section class="blog">
  <h2 class="section-title">Recent Blog</h2>
  <span class="rule"></span>
  <div class="blog-grid">
    <article class="post">
      <div class="post-photo" role="img" aria-label="Rows of open electrical control cabinets"></div>
      <div class="date"><div class="day">12 Nov</div><div class="year">2017</div><div class="count">8</div></div>
      <div class="post-body">
        <h3>Lorem Ipsum is simply dummy</h3>
        <p>Notes from a recent panel upgrade: planning the shutdown, labelling circuits and testing before restart.</p>
      </div>
      <div class="post-meta"><span>Site Team &nbsp;·&nbsp; Field</span><a href="#">Learn More »</a></div>
    </article>
    <article class="post">
      <div class="post-photo" role="img" aria-label="Grain storage silos at an industrial site"></div>
      <div class="date"><div class="day">12 Nov</div><div class="year">2017</div><div class="count">8</div></div>
      <div class="post-body">
        <h3>Lorem Ipsum is simply dummy</h3>
        <p>How we aligned conveyors and drives at a grain site while keeping the loading schedule on track.</p>
      </div>
      <div class="post-meta"><span>Site Team &nbsp;·&nbsp; Field</span><a href="#">Learn More »</a></div>
    </article>
  </div>
</section>

<section class="clients">
  <h2>Our Clients</h2>
  <div class="client-row">
    <svg class="client-arrow" viewBox="0 0 16 28"><path d="M13 3 3 14l10 11" fill="none" stroke="#0e2b45" stroke-width="3"/></svg>
    <span class="client"><i></i>MarlowKibbleCo</span>
    <span class="client"><i></i>Dunholt University</span>
    <span class="client"><i></i>OKSU</span>
    <span class="client"><i></i>Tazzik</span>
    <svg class="client-arrow" viewBox="0 0 16 28"><path d="M3 3l10 11L3 25" fill="none" stroke="#0e2b45" stroke-width="3"/></svg>
  </div>
</section>

<footer class="site-footer">
  <div class="footer-brand">
    <div class="brand"><span class="brand-name">BRIVAN</span><span class="brand-sub">HOLDINGS LTD</span></div>
    <p>Electrical, automation and millwright services for industry.</p>
  </div>
  <div class="contact">
    <h3>Contact Us</h3>
    <ul>
      <li><svg viewBox="0 0 14 14"><path d="M3 1l3 3-2 2a8 8 0 0 0 4 4l2-2 3 3-2 2C5 13 1 9 1 3z" fill="#1ba0e1"/></svg>Call Us 0 (555) 014 2290</li>
      <li><svg viewBox="0 0 14 14"><rect x="1" y="3" width="12" height="8" fill="none" stroke="#1ba0e1" stroke-width="1.5"/><path d="M1 3l6 5 6-5" fill="none" stroke="#1ba0e1" stroke-width="1.5"/></svg>info@brivanholdings.net</li>
      <li><svg viewBox="0 0 14 14"><path d="M7 13S2 8 2 5a5 5 0 0 1 10 0c0 3-5 8-5 8z" fill="#1ba0e1"/><circle cx="7" cy="5" r="1.8" fill="#0e2b45"/></svg>Ridgefield, USA</li>
    </ul>
  </div>
  <div class="footer-right">
    <nav class="footer-nav"><a href="#">Home</a><a href="#">About Us</a><a href="#">Services</a><a href="#">Our Projects</a><a href="#">Contact Us</a></nav>
    <h3>Newsletter</h3>
    <div class="newsletter"><span>Your Email</span><b>Subscribe</b></div>
  </div>
</footer>

</body>
</html>
```